New Business Card Design Project - Marlo Constructions

We would like a business card for business specialising in timber framed houses in Western Australia.

We need it to be professional and high-end style (not tacky) but manly (not girly).

We would like to have a timber/wooden NZ fern as a symbol/logo (or similar) and also a black sketched/graphically designed timber framed house somewhere on the card (red may also be a colour we would like featured).

We would also like details such business name, sole trader name, mobile number, website address and email address listed.

We would also like catch phrases or bullet points to include:
- Specialising in timber/stud frame houses
- New houses/extensions
- Decks/pergolas
- Iron roofs/fascia/guttering
- Fencing/patios
- Doors/skirting/shelves
- Anything involving timber

Note: We would like to know what text you have used to create the card.

Please let us know if you require any further details.

```html
<!DOCTYPE html>
<html lang="en">
<head>
<meta charset="utf-8">
<title>Marlo Constructions – Business Card</title>
<link rel="stylesheet" href="https://fonts.googleapis.com/css2?family=Quicksand:wght@300;400;600&display=swap">
<style>
  :root {
    --stage: #2b2420;
    --wood-dark: #4a2c1a;
    --wood-mid: #7a4a2c;
    --wood-light: #9a6240;
    --ink-light: #f3ece4;
    --ink-engraved: #3a2114;
  }
  * { margin: 0; padding: 0; box-sizing: border-box; }
  html, body {
    width: 1200px; height: 1000px; overflow: hidden;
    background: var(--stage);
    font-family: "Quicksand", sans-serif;
  }
  .stage {
    width: 1200px; height: 1000px;
    display: flex; align-items: center; justify-content: center; gap: 40px;
  }
  .card {
    position: relative;
    width: 540px; height: 310px;
    overflow: hidden;
    box-shadow: 0 10px 30px rgba(0,0,0,.45);
  }
  .card__wood {
    position: absolute; inset: 0;
    background: linear-gradient(100deg, var(--wood-dark) 0%, var(--wood-mid) 45%, var(--wood-light) 60%, var(--wood-mid) 80%, var(--wood-dark) 100%);
  }
  /* back side */
  .card--back .holder-name {
    position: absolute; top: 58px; left: 352px;
    color: var(--ink-light); font-weight: 400; font-size: 22px; letter-spacing: .5px;
  }
  .contact-list {
    position: absolute; top: 58px; right: 210px;
    list-style: none; color: var(--ink-light);
    font-weight: 300; font-size: 11.5px; line-height: 22px;
  }
  .contact-list li { display: flex; align-items: center; justify-content: flex-end; gap: 14px; }
  .contact-list svg { width: 13px; height: 13px; flex: none; }
  .services {
    position: absolute; left: 0; right: 0; top: 200px;
    text-align: center; color: var(--ink-light);
    font-weight: 300; font-size: 11.5px; line-height: 20px; letter-spacing: .6px;
  }
  /* front side */
  .card--front { display: flex; align-items: center; justify-content: center; }
  .brand {
    position: relative; display: flex; align-items: center; gap: 16px;
  }
  .brand__dot {
    width: 22px; height: 22px; border-radius: 50%; background: var(--ink-engraved);
  }
  .brand__name {
    color: var(--ink-engraved); font-weight: 600; font-size: 34px;
    letter-spacing: 5px; text-transform: uppercase; line-height: 1.15;
  }
</style>
</head>
<body>
<main class="stage">
  <section class="card card--back" aria-label="Business card, back">
    <div class="card__wood" role="img" aria-label="Dark timber plank texture"></div>
    <h2 class="holder-name">Rowan Hale</h2>
    <ul class="contact-list">
      <li>0400 218 736
        <svg viewBox="0 0 16 16" aria-hidden="true"><path fill="#f3ece4" d="M3 1h3l1 4-2 1a9 9 0 0 0 5 5l1-2 4 1v3a2 2 0 0 1-2 2A13 13 0 0 1 1 3a2 2 0 0 1 2-2z"/></svg></li>
      <li>14 Karri Road Bunbury WA 6230
        <svg viewBox="0 0 16 16" aria-hidden="true"><path fill="#f3ece4" d="M8 0a5 5 0 0 1 5 5c0 4-5 11-5 11S3 9 3 5a5 5 0 0 1 5-5zm0 3a2 2 0 1 0 0 4 2 2 0 0 0 0-4z"/></svg></li>
      <li>rowan@marloconstructions.au
        <svg viewBox="0 0 16 16" aria-hidden="true"><rect x="1" y="3" width="14" height="10" fill="#f3ece4"/><path d="M1 3l7 6 7-6" fill="none" stroke="#5a3520" stroke-width="1.2"/></svg></li>
      <li>marloconstructions.au
        <svg viewBox="0 0 16 16" aria-hidden="true"><circle cx="8" cy="8" r="6" fill="#f3ece4"/></svg></li>
    </ul>
    <p class="services">
      - Specialising in timber/stud frame houses - New houses/extensions -<br>
      Decks/pergolas - Iron roofs/fascia/guttering - Fencing/patios<br>
      - Doors/skirting/shelves - Anything involving timber -
    </p>
  </section>

  <section class="card card--front" aria-label="Business card, front">
    <div class="card__wood" role="img" aria-label="Warm timber plank texture"></div>
    <div class="brand">
      <span class="brand__dot" aria-hidden="true"></span>
      <h1 class="brand__name">Marlo<br>Constructions</h1>
    </div>
  </section>
</main>
</body>
</html>
```